Psychiatrist/ Psychotherapist needs a letterhead design

I am a Psychiatrist working in private practice. I work as a psychotherapist and treat patients with depression, anxiety, post traumatic stress and relationship problems. I need a letterhead which is elegant and professional. I would like to see designs using colours such as blues and greys.
I would like the information on the letterhead split between the top and bottom of the page to give it a look of balance.
I want it to look elegant, feminine and upmarket. I don't want it to look too corporate but to show some flair and to be a bit artistic.

Other doctors, specialists and agencies who have referred patients to me.

Work

Script

Requirements
Must have
• My name and my profession psychiatrist need to be highlighted and prominent. It needs to be professional looking and elegant without being old fashioned or too conservative.
Nice to have
• Balance between the top and bottom of the page.
Should not have
• I don't want fonts which are old and too traditional.

```html
<!DOCTYPE html>
<html lang="en">
<head>
<meta charset="utf-8">
<title>Letterhead – Dr Clara Whitfield</title>
<link rel="stylesheet" href="https://fonts.googleapis.com/css2?family=Dancing+Script:wght@400&family=Questrial&display=swap">
<style>
  :root {
    --backdrop: #b7b8ba;
    --paper: #ffffff;
    --brand-blue: #2a63a8;
    --band-blue: #2460a4;
    --accent-blue: #1f86e6;
    --text-grey: #8a8d91;
    --mark-grey: #ececec;
  }
  * { margin: 0; padding: 0; box-sizing: border-box; }
  html, body {
    width: 1200px; height: 1013px; overflow: hidden;
    background: var(--backdrop);
  }
  .letterhead {
    position: absolute; left: 376px; top: 165px;
    width: 428px; height: 612px;
    background: var(--paper);
    border-left: 2px solid var(--brand-blue);
    font-family: "Questrial", "Helvetica Neue", Arial, sans-serif;
    overflow: hidden;
  }
  .header { position: absolute; left: 34px; top: 28px; }
  .doctor-name {
    font-family: "Dancing Script", cursive;
    font-weight: 400; font-size: 27px; line-height: 1;
    color: var(--brand-blue); white-space: nowrap;
  }
  .doctor-name .degree { color: var(--text-grey); }
  .profession {
    margin-top: 18px; font-size: 12.5px; letter-spacing: 0.3px;
    color: var(--text-grey);
  }
  .profession .divider { margin: 0 4px; }
  .profession .role { color: var(--brand-blue); }
  .contact { margin-top: 5px; list-style: none; font-size: 10px; color: var(--text-grey); }
  .contact li { display: flex; align-items: center; gap: 4px; line-height: 13px; }
  .contact svg { width: 9px; height: 9px; flex: none; }
  .head-motif {
    position: absolute; left: 34px; top: 448px;
    width: 122px; height: 164px;
    background: var(--mark-grey);
    border-radius: 60px 60px 0 0;
  }
  .footer-band { position: absolute; left: 0; bottom: 0; width: 428px; height: 46px; }
  .footer-address {
    position: absolute; right: 6px; bottom: 4px;
    text-align: right; font-size: 9.5px; line-height: 12px;
    color: #ffffff; letter-spacing: 0.3px;
  }
</style>
</head>
<body>
  <main class="letterhead">
    <header class="header">
      <h1 class="doctor-name">Dr Clara Whitfield <span class="degree">B.Med</span></h1>
      <p class="profession">FRANZCP<span class="divider">|</span><span class="role">Psychiatrist</span></p>
      <ul class="contact">
        <li>
          <svg viewBox="0 0 10 10" aria-hidden="true"><rect x="2.5" y="0.5" width="5" height="9" rx="1" fill="none" stroke="#2a63a8" stroke-width="1"/><rect x="3.5" y="1.8" width="3" height="4" fill="#2a63a8"/></svg>
          <span>0412578904</span>
        </li>
        <li>
          <svg viewBox="0 0 10 10" aria-hidden="true"><rect x="0.5" y="2" width="9" height="6" fill="none" stroke="#2a63a8" stroke-width="1"/><path d="M0.5 2 L5 5.5 L9.5 2" fill="none" stroke="#2a63a8" stroke-width="1"/></svg>
          <span>cwhitfield@mailbox.net.au</span>
        </li>
      </ul>
    </header>

    <div class="head-motif" role="img" aria-label="Faint grey illustration of a head in profile with a brain"></div>

    <svg class="footer-band" viewBox="0 0 428 46" aria-hidden="true">
      <polygon points="0,39 428,6 428,46 0,46" fill="var(--band-blue)"/>
      <polygon points="0,34 428,0 428,4 0,38" fill="var(--accent-blue)"/>
    </svg>
    <address class="footer-address">
      12 Linden Avenue, Norwood, SA 5067<br>
      FAX: (08) 8126 4471
    </address>
  </main>
</body>
</html>
```